Skin Care Logo and Package Design

We need a Logo and Label design for our new skin care line we are launching in our medical spa here in Atlanta. Our medical spa provides high end skin care and body contouring treatments like Vantrelle, laser treatments, facials and chemical peels. I would like to see a clean, sleek, modern feel. i am attaching a picture of the packaging we will being using. Please keep in mind the Serum and Cream jar containers will be packaged in a white box. This packaging is the Dorvain packaging in attached document.) The tall bottles (Willowmere Collection) will be for facial cleansers and body lotions, these will not have a box. Please refer to attached file. Thank you.

Target Market(s)

Anti-Aging men and women age 30 to 65

Requirements
Must have
• Logo: the name of the product: Velmora Clinical
Design and lay out for Bottle: See attached download of packaging, Face cleanser bottle is the "Willowmere" Collection, this bottle will be used for all cleansers, toners, and body lotions.
Design and lay out for Serum and Face cream package: This will be the "Dorvain" Collection, see attached pdf for picture. Both products will have white boxes so we will need a designed label for box.

Also, I have included our company logo to our med spa. I wouldn't mind something that follows close to our brand.
Nice to have
• Like to have a modern, sophisticated, yet simple. Maybe add a nature flair to the design?
Should not have
• Lots of Color

```html
<!DOCTYPE html>
<html lang="en">
<head>
<meta charset="UTF-8">
<title>Velmora Clinical – Label Set</title>
<link rel="stylesheet" href="https://fonts.googleapis.com/css2?family=Montserrat:wght@300;400;500&display=swap">
<style>
  :root {
    --canvas: #ffffff;
    --label: #f8f7f4;
    --label-edge: #e4e1dc;
    --ink: #1f1f26;
    --ink-soft: #55555d;
    --rule: #8a8a90;
  }
  * { box-sizing: border-box; margin: 0; padding: 0; }
  html, body {
    width: 1200px;
    height: 851px;
    overflow: hidden;
    background: var(--canvas);
    font-family: "Montserrat", sans-serif;
    color: var(--ink);
  }
  .label-set {
    width: 1200px;
    height: 851px;
    display: flex;
    align-items: flex-end;
    justify-content: center;
    gap: 30px;
    padding-bottom: 150px;
  }
  .label {
    background: var(--label);
    border: 1px solid var(--label-edge);
    display: flex;
    flex-direction: column;
    align-items: center;
    text-align: center;
  }
  .brand {
    display: flex;
    flex-direction: column;
    align-items: center;
  }
  .brand--inline {
    flex-direction: row;
    gap: 10px;
  }
  .brand__dot {
    width: 18px;
    height: 18px;
    border: 1.5px solid var(--ink);
    border-radius: 50%;
  }
  .brand__text { display: flex; flex-direction: column; align-items: center; }
  .brand__name {
    font-weight: 400;
    letter-spacing: 0.18em;
    text-transform: uppercase;
    font-size: 16px;
    line-height: 1.1;
  }
  .brand__sub {
    font-weight: 400;
    letter-spacing: 0.35em;
    text-transform: uppercase;
    font-size: 8px;
    margin-top: 3px;
  }
  .product-name {
    font-weight: 500;
    letter-spacing: 0.3em;
    text-transform: uppercase;
    font-size: 9px;
    padding: 6px 4px;
    border-top: 1px solid var(--rule);
    border-bottom: 1px solid var(--rule);
  }
  .claims {
    font-size: 5px;
    letter-spacing: 0.35em;
    text-transform: uppercase;
    line-height: 2.4;
    color: var(--ink-soft);
  }
  .craft {
    font-size: 5px;
    letter-spacing: 0.05em;
    line-height: 1.4;
    color: var(--ink-soft);
  }
  .origin {
    font-size: 5px;
    letter-spacing: 0.3em;
    text-transform: uppercase;
    color: var(--ink-soft);
    padding: 4px 10px;
    border-top: 1px solid var(--rule);
    border-bottom: 1px solid var(--rule);
  }

  /* individual labels */
  .label--jar { width: 200px; height: 130px; justify-content: center; }
  .label--night { width: 150px; height: 300px; padding-top: 40px; gap: 18px; }
  .label--night .product-name { font-size: 7px; }
  .label--day { width: 180px; height: 420px; padding-top: 60px; gap: 22px; }
  .label--day .brand__name { font-size: 18px; }
  .label--cleanser { width: 220px; height: 190px; justify-content: center; gap: 20px; }
  .label--cleanser .product-name { letter-spacing: 0.8em; padding-left: 12px; }
  .label--complex { width: 260px; height: 140px; justify-content: center; gap: 14px; }
  .label--complex .product-name { letter-spacing: 0.45em; }
</style>
</head>
<body>
  <main class="label-set">

    <section class="label label--jar">
      <div class="brand brand--inline">
        <span class="brand__dot"></span>
        <div class="brand__text">
          <span class="brand__name">Velmora</span>
          <span class="brand__sub">Clinical</span>
        </div>
      </div>
    </section>

    <section class="label label--night">
      <div class="brand">
        <span class="brand__dot"></span>
        <span class="brand__name" style="margin-top:10px">Velmora</span>
        <span class="brand__sub">Clinical</span>
      </div>
      <h2 class="product-name">Nightcream</h2>
      <p class="claims">Finest<br>Nantural<br>Fragrances</p>
      <p class="craft">high quality craftsmanship<br>all natural ingredients</p>
      <p class="origin">Made in USA</p>
    </section>

    <section class="label label--day">
      <div class="brand">
        <span class="brand__dot"></span>
        <span class="brand__name" style="margin-top:12px">Velmora</span>
        <span class="brand__sub">Clinical</span>
      </div>
      <h2 class="product-name" style="margin-top:40px">Daycream</h2>
      <p class="claims">Finest<br>Nantural<br>Fragrances</p>
      <p class="craft">high quality craftsmanship<br>all natural ingredients</p>
      <p class="origin">Made in USA</p>
    </section>

    <section class="label label--cleanser">
      <div class="brand">
        <span class="brand__dot"></span>
        <span class="brand__name" style="margin-top:10px">Velmora</span>
        <span class="brand__sub">Clinical</span>
      </div>
      <h2 class="product-name">Cleanser</h2>
    </section>

    <section class="label label--complex">
      <div class="brand brand--inline">
        <span class="brand__dot"></span>
        <div class="brand__text">
          <span class="brand__name">Velmora</span>
          <span class="brand__sub">Clinical</span>
        </div>
      </div>
      <h2 class="product-name">Anti Aging Complex</h2>
    </section>

  </main>
</body>
</html>
```